Thornfield Marsh, LLC Website

We are a small law firm in need of a website that contains the following:
1. Attractive main page
2. About us/attorney info for three people: Leonard Thornfield (attorney), Brent Marsh (attorney), and Melinda Carrow (legal assistant). We have bio's ready to submit.
3. Blog/video page. We'd like to post blogs and videos to help drive traffic
4. Multidistrict Litigation and Class Actions page, where we post information regarding active MDLs and Class actions that we are doing intake on.
Updates

Can you also please use the color "gold" in the design and logo? Thanks.

Industry/Entity Type

Legal

Coding

Coded - Design and coding required

Number of Pages Required

1 page

Colors
0054AA
0677BA
7BADD7
CADEEF
E8F1F8

Requirements
Must have
• 1. Attractive main page 2. About us/attorney info for three people: Leonard Thornfield (attorney), Brent Marsh (attorney), and Melinda Carrow (legal assistant). We have bio's ready to submit. 3. Blog/video page. We'd like to post blogs and videos to help drive traffic 4. Multidistrict Litigation and Class Actions page, where we post information regarding active MDLs and Class actions that we are doing intake on.

```html
<!DOCTYPE html>
<html lang="en">
<head>
<meta charset="utf-8">
<title>Thornfield Marsh, LLC — Lawyers</title>
<link href="https://fonts.googleapis.com/css2?family=Prata&family=Inter:wght@400;500;600&display=swap" rel="stylesheet">
<style>
:root{
  --ink:#0b1629;
  --navy:#162b4d;
  --gold:#b8924f;
  --gold-soft:#c9a46a;
  --white:#ffffff;
  --muted:#c9d2e0;
  --line:rgba(255,255,255,.18);
}
*{box-sizing:border-box;margin:0;padding:0}
html,body{width:1200px;height:3876px;overflow:hidden}
body{position:relative;background:var(--ink);font-family:"Inter",sans-serif;color:var(--white)}
.serif{font-family:"Prata",serif;font-weight:400}
.abs{position:absolute}
.btn{position:absolute;display:flex;align-items:center;justify-content:center;font-size:10px;font-weight:600;color:var(--white)}
.btn-gold{background:var(--gold)}
.btn-navy{background:var(--navy)}
.band{position:absolute;left:0;width:1200px}
.photo{position:absolute}

/* header */
.site-header{top:0;height:62px;background:var(--ink)}
.brand{left:107px;top:15px;height:33px;width:180px;border:1.5px solid var(--white);display:flex;align-items:center;gap:8px;padding-left:8px;font-weight:600;font-size:13px;color:var(--gold)}
.brand-square{width:16px;height:16px;background:var(--gold)}
.nav{left:412px;top:25px;display:flex;gap:18px;font-size:10px}
.nav .current{color:var(--gold)}
.nav-phone{left:821px;top:23px;font-size:12px;font-weight:500;display:flex;gap:6px;align-items:center}

/* hero */
.hero{top:62px;height:469px;background:linear-gradient(100deg,#e8e9ec 0%,#f4f4f4 45%,#d9dbe2 75%,#b9bfcd 100%)}
.hero h1{position:absolute;left:0;width:1200px;top:128px;text-align:center;font-size:57px;line-height:72px;color:#14223a}

/* intro */
.intro{top:531px;height:484px;background:var(--ink)}
.pill{left:107px;top:102px;width:248px;height:158px;border-radius:79px;background:linear-gradient(135deg,#d9d9d9,#8a8a8a)}
.years{left:157px;top:279px;display:flex;align-items:center;gap:10px}
.years b{font-family:"Prata",serif;font-weight:400;font-size:40px}
.years span{font-size:10px;line-height:12px}
.intro h2{left:406px;top:100px;font-size:58px;line-height:71px}
.intro p{left:818px;top:131px;width:260px;font-size:10.5px;line-height:19px;color:var(--muted)}
.intro .rule{left:818px;top:235px;width:325px;height:1px;background:var(--line)}

/* services */
.services{top:1015px;height:675px;background:var(--navy)}
.stats{left:368px;top:938px;width:832px;height:155px;background:var(--gold);display:flex;align-items:center}
.stat{flex:1;padding-left:120px;height:92px;display:flex;flex-direction:column;justify-content:center;border-right:1px solid rgba(255,255,255,.5)}
.stat:last-child{border-right:none}
.stat b{font-family:"Prata",serif;font-weight:400;font-size:42px;line-height:48px}
.stat span{font-size:10px;line-height:12px;width:110px}
.section-title{position:absolute;left:0;width:1200px;text-align:center;font-size:45px;line-height:55px}
.service-card{position:absolute;top:1310px;width:481px;height:236px;border:1px solid rgba(255,255,255,.55)}
.service-card .photo{left:0;top:0;width:181px;height:100%}
.service-card h3{position:absolute;left:211px;top:32px;font-size:20px}
.service-card p{position:absolute;left:211px;top:76px;width:240px;font-size:10px;line-height:19px;color:var(--muted)}
.circle-arrow{position:absolute;left:211px;top:168px;width:30px;height:30px;border:1px solid var(--gold);border-radius:50%}

/* team */
.team{top:1690px;height:739px;background:var(--ink)}
.member{position:absolute;top:1906px;width:250px;text-align:center}
.member .photo{position:relative;width:250px;height:311px}
.member-icons{position:absolute;left:0;width:250px;top:300px;display:flex;justify-content:center;gap:6px}
.member-icons span{width:24px;height:24px;border-radius:50%;background:var(--ink);border:1px solid var(--white);display:flex;align-items:center;justify-content:center}
.member h4{margin-top:30px;font-size:14px}
.member small{display:block;margin-top:6px;font-size:9px;color:var(--gold)}

/* testimonials */
.voices{top:2429px;height:453px;background:var(--gold)}
.voices-title{left:200px;top:2500px;font-size:45px;line-height:55px}
.avatar{position:absolute;top:2644px;width:69px;height:69px;border-radius:50%;border:3px solid rgba(255,255,255,.55)}
.client-name{left:277px;top:2731px;text-align:center;width:104px;font-size:12px}
.client-name small{display:block;font-family:"Inter",sans-serif;font-size:9px;margin-top:2px}
.quote{left:505px;top:2647px;width:480px;font-size:10.5px;line-height:19px}
.round-btn{position:absolute;top:2776px;width:30px;height:30px;border-radius:50%;border:1px solid var(--white);display:flex;align-items:center;justify-content:center}

/* blog */
.blog{top:2882px;height:660px;background:var(--ink)}
.post{position:absolute;top:3097px;width:250px;height:299px;border:1px solid rgba(255,255,255,.3)}
.post .photo{left:0;top:0;width:100%;height:156px}
.post .date{position:absolute;left:18px;top:178px;font-size:9px;color:var(--gold)}
.post h5{position:absolute;left:18px;top:202px;width:215px;font-size:13px;line-height:19px}
.post .more{position:absolute;left:18px;top:268px;font-size:9px;font-weight:600;color:var(--gold)}
.play{position:absolute;left:103px;top:128px;width:44px;height:44px;border-radius:50%;background:var(--white);display:flex;align-items:center;justify-content:center}

/* footer */
.site-footer{top:3542px;height:334px;background:var(--navy)}
.f-label{left:107px;top:3617px;font-size:12px;font-weight:600}
.f-title{left:107px;top:3648px;font-size:42px;color:var(--gold)}
.f-text{left:107px;top:3710px;width:340px;font-size:9.5px;line-height:15px;color:var(--muted)}
.f-icon{position:absolute;top:3647px;width:36px;height:36px;border-radius:50%;border:1px solid rgba(255,255,255,.35);display:flex;align-items:center;justify-content:center}
.f-block{position:absolute;top:3655px;font-size:10px;line-height:16px}
.f-block h6{font-size:12px;font-weight:600;color:var(--gold);margin-bottom:4px}
.f-block a{color:var(--gold);font-size:9px;font-weight:600;text-decoration:none}
.social{position:absolute;left:1063px;width:30px;height:30px;border-radius:50%;border:1px solid var(--gold)}
.f-rule{left:107px;top:3805px;width:986px;height:1px;background:var(--line)}
.copy{left:107px;top:3830px;font-size:9.5px}
.copy em{font-style:normal;color:var(--gold)}
.f-nav{left:523px;top:3830px;display:flex;gap:18px;font-size:9.5px}
.f-nav .current{color:var(--gold)}
.to-top{left:1140px;top:3808px}
</style>
</head>
<body>

<header class="band site-header">
  <div class="abs brand"><span class="brand-square"></span>Thornfield Marsh, LLC</div>
  <nav class="abs nav">
    <span class="current">Home</span><span>About Us</span><span>Multidistrict Litigation</span><span>Class Actions</span><span>Blog</span><span>Contact Us</span>
  </nav>
  <div class="abs nav-phone">
    <svg width="13" height="13" viewBox="0 0 24 24" fill="none" stroke="#fff" stroke-width="2"><path d="M5 3h4l2 5-3 2a11 11 0 0 0 6 6l2-3 5 2v4a2 2 0 0 1-2 2A17 17 0 0 1 3 5a2 2 0 0 1 2-2z"/></svg>
    (555) 014-2290
  </div>
  <div class="btn btn-gold" style="left:957px;top:13px;width:136px;height:35px">Free Case Evaluation</div>
</header>

<section class="band hero" role="img" aria-label="Bright office desk with a gavel, golden scales of justice and a lawyer's hand resting on papers">
  <h1 class="serif">A law firm with a<br>passion for sucesss</h1>
  <div class="btn btn-gold" style="left:538px;top:305px;width:122px;height:34px">Contcat Us Today!</div>
</section>

<section class="band intro">
  <div class="photo pill" role="img" aria-label="Black and white photo of three lawyers meeting at a table"></div>
  <div class="abs years"><b>25+</b><span>Years<br>experiences</span></div>
  <h2 class="abs serif">We proudly<br>fight for your<br>rights</h2>
  <p class="abs">Lorem Ipsum is simply dummy text of the printing and typesetting industry lorem Ipsum has been the industry's standard dummy text ever since the unknown.</p>
  <div class="abs rule"></div>
  <div class="btn btn-navy" style="left:818px;top:266px;width:105px;height:36px">Discover More</div>
</section>

<section class="band services"></section>
<div class="abs stats">
  <div class="stat"><b>1.3K+</b><span>Critical cases solved successfully</span></div>
  <div class="stat" style="padding-left:78px"><b>55+</b><span>Established fact work that reader</span></div>
  <div class="stat" style="padding-left:78px"><b>12+</b><span>standard dummy achievement</span></div>
</div>
<h2 class="section-title serif" style="top:1167px">We are provided especially<br>services to you.</h2>

<article class="service-card" style="left:107px">
  <div class="photo" role="img" aria-label="Miniature building model held in a hand beside a gavel and scales" style="background:linear-gradient(135deg,#e0b070,#7a5a3a)"></div>
  <h3 class="serif">Multidistrict Litigation</h3>
  <p>Lorem Ipsum is simply dummy text of the work printing and typesetting industry lorem Ipsum has been the industry's standard dummy text ever since the unknown.</p>
  <span class="circle-arrow"><svg width="30" height="30" viewBox="0 0 30 30" fill="none" stroke="#b8924f" stroke-width="1.3"><path d="M12 18l6-6M13 12h5v5"/></svg></span>
</article>
<article class="service-card" style="left:612px">
  <div class="photo" role="img" aria-label="Wooden gavel, fountain pen and scales on a desk" style="background:linear-gradient(135deg,#e9e4dc,#8a5a3c)"></div>
  <h3 class="serif">Class Actions</h3>
  <p>Lorem Ipsum is simply dummy text of the work printing and typesetting industry lorem Ipsum has been the industry's standard dummy text ever since the unknown.</p>
  <span class="circle-arrow"><svg width="30" height="30" viewBox="0 0 30 30" fill="none" stroke="#b8924f" stroke-width="1.3"><path d="M12 18l6-6M13 12h5v5"/></svg></span>
</article>
<div class="btn btn-gold" style="left:531px;top:1579px;width:137px;height:35px">Free Case Evaluation</div>

<section class="band team"></section>
<h2 class="section-title serif" style="top:1762px">We provide our advance level<br>of legal support</h2>

<div class="member" style="left:200px">
  <div class="photo" role="img" aria-label="Portrait of attorney Leonard Thornfield in a dark suit" style="background:linear-gradient(180deg,#d9c9a0,#3a3a40)"></div>
  <div class="member-icons"><span><svg width="11" height="11" viewBox="0 0 24 24" fill="none" stroke="#fff" stroke-width="2"><path d="M5 3h4l2 5-3 2a11 11 0 0 0 6 6l2-3 5 2v4a2 2 0 0 1-2 2A17 17 0 0 1 3 5a2 2 0 0 1 2-2z"/></svg></span><span><svg width="11" height="11" viewBox="0 0 24 24" fill="none" stroke="#fff" stroke-width="2"><rect x="3" y="5" width="18" height="14"/><path d="M3 6l9 7 9-7"/></svg></span></div>
  <h4 class="serif">Leonard Thornfield</h4><small>Attorney</small>
</div>
<div class="member" style="left:475px">
  <div class="photo" role="img" aria-label="Portrait of attorney Brent Marsh in a green suit" style="background:linear-gradient(180deg,#4a5a4a,#1f3a3a)"></div>
  <div class="member-icons"><span><svg width="11" height="11" viewBox="0 0 24 24" fill="none" stroke="#fff" stroke-width="2"><path d="M5 3h4l2 5-3 2a11 11 0 0 0 6 6l2-3 5 2v4a2 2 0 0 1-2 2A17 17 0 0 1 3 5a2 2 0 0 1 2-2z"/></svg></span><span><svg width="11" height="11" viewBox="0 0 24 24" fill="none" stroke="#fff" stroke-width="2"><rect x="3" y="5" width="18" height="14"/><path d="M3 6l9 7 9-7"/></svg></span></div>
  <h4 class="serif">Brent Marsh</h4><small>Attorney</small>
</div>
<div class="member" style="left:750px">
  <div class="photo" role="img" aria-label="Portrait of legal assistant Melinda Carrow in a navy suit" style="background:linear-gradient(180deg,#c8d8e4,#2a3a5a)"></div>
  <div class="member-icons"><span><svg width="11" height="11" viewBox="0 0 24 24" fill="none" stroke="#fff" stroke-width="2"><path d="M5 3h4l2 5-3 2a11 11 0 0 0 6 6l2-3 5 2v4a2 2 0 0 1-2 2A17 17 0 0 1 3 5a2 2 0 0 1 2-2z"/></svg></span><span><svg width="11" height="11" viewBox="0 0 24 24" fill="none" stroke="#fff" stroke-width="2"><rect x="3" y="5" width="18" height="14"/><path d="M3 6l9 7 9-7"/></svg></span></div>
  <h4 class="serif">Melinda Carrow</h4><small>legal Assistant</small>
</div>
<div class="btn btn-navy" style="left:550px;top:2318px;width:100px;height:36px">Explore More</div>

<section class="band voices"></section>
<h2 class="abs serif voices-title">What people are<br>saying</h2>
<div class="avatar" role="img" aria-label="Client portrait" style="left:200px;background:#cfae7a"></div>
<div class="avatar" role="img" aria-label="Client portrait of Carla Benton" style="left:293px;background:#f0e4d6;border-color:#fff"></div>
<div class="avatar" role="img" aria-label="Client portrait" style="left:388px;background:#d6ac74"></div>
<div class="abs client-name serif">Carla Benton<small>Costumer</small></div>
<div class="abs quote">
  <p>Lorem ipsum is simply dummy text of the printing and typesetting industry. lorem ipsum has been the industry's standard dummy text ever since the 1500s, when an unknown printer took a galley of type and scrambled it to make a type specimen book.</p>
  <p style="margin-top:12px;width:300px">Lorem ipsum is simply dummy text of the printing and typesetting industry lorem ipsum...</p>
</div>
<span class="round-btn" style="left:506px"><svg width="10" height="10" viewBox="0 0 10 10" fill="none" stroke="#fff" stroke-width="1.3"><path d="M6 2L3 5l3 3"/></svg></span>
<span class="round-btn" style="left:544px"><svg width="10" height="10" viewBox="0 0 10 10" fill="none" stroke="#fff" stroke-width="1.3"><path d="M4 2l3 3-3 3"/></svg></span>

<section class="band blog"></section>
<h2 class="section-title serif" style="top:2955px">Our advice to people.</h2>
<p class="abs" style="left:0;width:1200px;top:3027px;text-align:center;font-size:10.5px">Lorem Ipsum is simply dummy text of the printing.</p>

<article class="post" style="left:200px">
  <div class="photo" role="img" aria-label="Lawyer signing documents at a desk with a laptop" style="background:linear-gradient(135deg,#a08060,#e8e4dc)"></div>
  <span class="date">Jan. 8, 2025</span>
  <h5 class="serif">Contrary to popular belief, lorem ipsum is not simply random text classical latin</h5>
  <span class="more">Read More ↗</span>
</article>
<article class="post" style="left:475px;border:none">
  <div class="photo" role="img" aria-label="Video still of two professionals shaking hands" style="height:299px;background:linear-gradient(135deg,#3a4a5a,#1a2430)"></div>
  <span class="play"><svg width="14" height="14" viewBox="0 0 14 14"><path d="M4 2l8 5-8 5z" fill="#0b1629"/></svg></span>
</article>
<article class="post" style="left:750px">
  <div class="photo" role="img" aria-label="Lawyer explaining a document to a client across a table" style="background:linear-gradient(135deg,#d8d8d8,#7a4a30)"></div>
  <span class="date">Feb. 10, 2025</span>
  <h5 class="serif">Contrary to popular belief, lorem ipsum is not simply random text classical latin</h5>
  <span class="more">Read More ↗</span>
</article>
<div class="btn btn-navy" style="left:550px;top:3429px;width:100px;height:36px">View All Blog</div>

<footer class="band site-footer"></footer>
<div class="abs f-label">Contact us</div>
<h2 class="abs serif f-title">Get in touch</h2>
<p class="abs f-text">Lorem ipsum is simply dummy text of the printing and typesetting industry. lorem ipsum has been the industry's standard dummy text ever galley of type and type specimen book.</p>

<span class="f-icon" style="left:524px"><svg width="14" height="14" viewBox="0 0 24 24" fill="none" stroke="#b8924f" stroke-width="1.6"><path d="M12 22s7-7 7-12a7 7 0 0 0-14 0c0 5 7 12 7 12z"/><circle cx="12" cy="10" r="2.5"/></svg></span>
<div class="f-block" style="left:574px">
  <h6>Address</h6>218 Harbor Lane, Bayport,<br>AL 36500<br><a>Get Directions ↗</a>
</div>
<span class="f-icon" style="left:776px"><svg width="14" height="14" viewBox="0 0 24 24" fill="none" stroke="#b8924f" stroke-width="1.6"><path d="M5 3h4l2 5-3 2a11 11 0 0 0 6 6l2-3 5 2v4a2 2 0 0 1-2 2A17 17 0 0 1 3 5a2 2 0 0 1 2-2z"/></svg></span>
<div class="f-block" style="left:826px">
  <h6>Contact Details</h6>info@thornfieldmarsh.com<br><span style="color:var(--gold);font-size:13px">(555) 014-2290</span>
</div>
<span class="social" style="top:3646px"></span>
<span class="social" style="top:3683px"></span>
<span class="social" style="top:3721px"></span>

<div class="abs f-rule"></div>
<div class="abs copy">© 2025 <em>Thornfield Marsh.</em> All rights reserved</div>
<nav class="abs f-nav"><span class="current">Home</span><span>About Us</span><span>Multidistrict Litigation</span><span>Class Actions</span><span>Blog</span><span>Contact Us</span></nav>
<svg class="abs to-top" width="16" height="18" viewBox="0 0 16 18"><path d="M8 0l8 18-8-5-8 5z" fill="#b8924f"/></svg>

</body>
</html>
```